Vitamin/Dietary Supplement Company needs a simple Hemp CBD Health retail website to display a few...

We need a simple website designed that will allow us to display a few products for purchase. We are a vitamin/dietary supplement company that wants to set up a separate website for CBD health products. CBD is a chemical compound found in hemp and cannabis plants that provide various health and medicinal benefits. Our target audience are individuals that suffer from health issues and would like to treat their pain relief with CBD as an alternative to prescription medication and over the counter drugs such as Paxorin and Dolvex. Looking for a simple and clean website that is easy for customers to navigate and purchase products.

Need extra days to review

Target Market(s)

Our target audience are individuals that suffer from health issues and would like to treat their pain relief with CBD as an alternative to prescription medication and over the counter drugs such as Paxorin and Dolvex.

Coding

Coded - Design and coding required

Font styles to use
Serif

Colors

Designer to choose colors to be used in the design.

Requirements
Nice to have
• Homepage, About page, FAQ page, Contact page, Blog page

```html
<!DOCTYPE html>
<html lang="en">
<head>
<meta charset="utf-8">
<title>Verdant Leaf – CBD Health Products</title>
<link rel="stylesheet" href="https://fonts.googleapis.com/css2?family=Sorts+Mill+Goudy&family=Lato:wght@400;700&display=swap">
<style>
:root{
  --green:#2f6a43;
  --green-dark:#285c3a;
  --text:#333333;
  --muted:#555555;
  --line:#dddddd;
  --footer-bg:#f2f2f2;
  --white:#ffffff;
}
*{box-sizing:border-box;margin:0;padding:0}
html,body{width:1200px;height:3220px;overflow:hidden}
body{position:relative;background:var(--white);font-family:"Lato",Arial,sans-serif;color:var(--text)}
a{color:inherit;text-decoration:none}
.serif{font-family:"Sorts Mill Goudy",Georgia,serif;font-weight:400}

/* utility bar */
.utility-bar{position:absolute;top:0;left:0;width:1200px;height:47px;background:var(--green);color:var(--white);font-size:15px;letter-spacing:.3px}
.utility-links{position:absolute;left:80px;top:14px;display:flex}
.utility-links a{padding:0 18px;border-left:1px solid rgba(255,255,255,.6)}
.utility-links a:first-child{padding-left:0;border-left:0}
.utility-phone{position:absolute;right:80px;top:13px;display:flex;align-items:center;gap:12px;font-size:17px}

/* header */
.site-header{position:absolute;top:47px;left:0;width:1200px;height:90px}
.brand{position:absolute;left:80px;top:24px;font-size:36px;color:var(--green)}
.search{position:absolute;left:833px;top:24px;width:288px;height:41px;background:#eeeeee;display:flex;align-items:center;padding:0 16px;font-size:14px;color:#888}
.search svg{position:absolute;right:14px;top:10px}

/* nav */
.main-nav{position:absolute;top:137px;left:0;width:1200px;height:50px;border-top:1px solid var(--line);border-bottom:1px solid var(--line);font-size:15px;color:var(--text)}
.main-nav ul{position:absolute;left:80px;top:15px;display:flex;list-style:none}
.main-nav li{padding:0 24px;border-left:1px solid #777;line-height:16px}
.main-nav li:first-child{padding-left:0;border-left:0;color:var(--green)}
.cart{position:absolute;right:80px;top:13px;display:flex;align-items:center;gap:12px}

/* hero */
.hero{position:absolute;top:187px;left:0;width:1200px;height:554px;overflow:hidden}
.hero-photo{position:absolute;inset:0;background:
  radial-gradient(ellipse at 40% 35%,#dfe8c8 0%,rgba(223,232,200,0) 45%),
  linear-gradient(100deg,#3f6a22 0%,#7ea34a 30%,#c9d7a8 55%,#b8c99a 70%,#4d7a2e 100%)}
.hero-product{position:absolute;left:795px;top:90px;width:330px;height:440px;border-radius:6px;background:linear-gradient(160deg,#e9f0e4,#4f8a3f 60%,#3b2a1c)}
.hero-title{position:absolute;left:80px;top:210px;font-size:42px;line-height:50px;color:var(--white);letter-spacing:1px;text-shadow:0 2px 4px rgba(0,0,0,.35)}
.hero-text{position:absolute;left:80px;top:272px;width:560px;font-size:20px;line-height:32px;color:var(--white);text-shadow:0 1px 3px rgba(0,0,0,.35)}

/* products */
.section-title{position:absolute;left:0;width:1200px;text-align:center;font-size:38px;color:var(--green);letter-spacing:.5px}
.product-grid{position:absolute;left:77px;display:grid;grid-template-columns:repeat(4,240px);column-gap:29px}
.product-card{position:relative;width:240px;height:405px;border:1px solid var(--line);background:var(--white);overflow:hidden}
.product-card.compact{height:395px}
.product-image{position:absolute;left:70px;top:44px;width:100px;height:170px;border-radius:10px}
.img-roll{background:linear-gradient(180deg,#f4f4f4,#e3efd2 60%,#8fbf5a)}
.img-pump{background:linear-gradient(180deg,#e8e8e8,#ffffff 40%,#2e6f73 75%,#ececec)}
.img-jar{left:50px;top:90px;width:140px;height:90px;border-radius:45px/20px;background:linear-gradient(180deg,#9ccc55,#f4f4f4 55%,#dcdcdc)}
.img-bottle{background:linear-gradient(180deg,#e8f0e4,#e34a2a 45%,#f2f2f2)}
.product-desc{position:absolute;left:20px;right:20px;top:256px;text-align:center;font-size:15px;line-height:25px;color:var(--muted)}
.compact .product-desc{top:250px}
.btn-cart{position:absolute;left:32px;top:326px;width:176px;height:40px;border-radius:20px;background:var(--green);color:var(--white);font-size:16px;font-weight:700;display:flex;align-items:center;justify-content:center}
.compact .btn-cart{top:314px}
.wish{position:absolute;right:16px;top:12px}
.ribbon{position:absolute;left:0;top:0}

/* welcome */
.welcome{position:absolute;top:1782px;left:0;width:1200px;height:416px;background:var(--green);color:var(--white);text-align:center}
.welcome h2{position:absolute;top:50px;width:100%;font-size:40px;letter-spacing:1px}
.welcome p{position:absolute;left:240px;width:720px;font-size:15.5px;line-height:25px}
.welcome .p1{top:112px}
.welcome .p2{top:230px}
.welcome-actions{position:absolute;top:296px;left:408px;display:flex;gap:12px}
.btn-light{width:186px;height:46px;border-radius:23px;background:var(--white);color:var(--green);font-size:16px;font-weight:700;display:flex;align-items:center;justify-content:center}

/* footer */
.footer-info{position:absolute;top:2793px;left:0;width:1200px;height:303px;background:var(--footer-bg);text-align:center;color:var(--muted)}
.footer-col{position:absolute;top:48px;height:210px;width:360px}
.footer-col h3{font-size:22px;color:var(--green);letter-spacing:.5px;margin-bottom:14px}
.footer-col p{font-size:15px;line-height:31px}
.col-hours{left:62px;padding-top:68px}
.col-contact{left:423px;width:359px;border-left:1px solid #cfcfcf;border-right:1px solid #cfcfcf;padding-top:26px}
.col-contact h3{margin-bottom:10px}
.col-contact .contact-intro{line-height:27px;padding:0 40px}
.col-social{left:782px;padding-top:46px}

.footer-bar{position:absolute;top:3096px;left:0;width:1200px;height:124px;background:var(--green);color:var(--white);text-align:center}
.footer-links{position:absolute;top:36px;width:100%;display:flex;justify-content:center;font-size:15px}
.footer-links a{padding:0 22px;border-left:1px solid rgba(255,255,255,.7);line-height:15px}
.footer-links a:first-child{border-left:0}
.copyright{position:absolute;top:78px;width:100%;font-size:14px}
</style>
</head>
<body>

<div class="utility-bar">
  <nav class="utility-links"><a href="#">MY ACCOUNT</a><a href="#">CBD RESOURCES</a><a href="#">CBD BULK/WHOLESALE</a></nav>
  <div class="utility-phone">
    <svg width="18" height="18" viewBox="0 0 24 24" fill="#fff"><path d="M6.6 10.8a15.1 15.1 0 0 0 6.6 6.6l2.2-2.2a1 1 0 0 1 1-.25 11.4 11.4 0 0 0 3.6.57 1 1 0 0 1 1 1V20a1 1 0 0 1-1 1A17 17 0 0 1 3 4a1 1 0 0 1 1-1h3.5a1 1 0 0 1 1 1c0 1.25.2 2.45.57 3.57a1 1 0 0 1-.25 1z"/></svg>
    <span>555 012 7788</span>
  </div>
</div>

<header class="site-header">
  <div class="brand serif">Verdant Leaf</div>
  <div class="search">Search
    <svg width="20" height="20" viewBox="0 0 24 24" fill="none" stroke="#2f6a43" stroke-width="2.4"><circle cx="10" cy="10" r="7"/><line x1="15" y1="15" x2="21" y2="21"/></svg>
  </div>
</header>

<nav class="main-nav">
  <ul><li>HOME</li><li>ABOUT US</li><li>FAQ</li><li>BLOG</li><li>CONTACT US</li></ul>
  <div class="cart">
    <svg width="24" height="22" viewBox="0 0 24 22" fill="none" stroke="#2f6a43" stroke-width="2"><path d="M2 8h20l-2.5 11h-15z"/><path d="M7 8l4-6M17 8l-4-6"/><line x1="9" y1="11" x2="9" y2="16"/><line x1="15" y1="11" x2="15" y2="16"/></svg>
    <span>MY CART</span>
  </div>
</nav>

<section class="hero">
  <div class="hero-photo" role="img" aria-label="Hemp leaves in soft sunlight"></div>
  <div class="hero-product" role="img" aria-label="CBD oil box and dropper bottle"></div>
  <h1 class="hero-title serif">CBD HEALTH PRODUCTS</h1>
  <p class="hero-text">Lorem Ipsum is simply dummy text of the printing and typesetting industry Lorem Ipsum has been the industry.</p>
</section>

<h2 class="section-title serif" style="top:787px">OUR PRODUCTS</h2>

<div class="product-grid" style="top:855px;row-gap:32px">
  <article class="product-card">
    <svg class="ribbon" width="100" height="100" viewBox="0 0 100 100"><polygon points="0,58 58,0 92,0 0,92" fill="#2f6a43"/><text x="39" y="45" transform="rotate(-45 39 39)" text-anchor="middle" font-family="Lato,sans-serif" font-weight="700" font-size="13" fill="#fff">NEW</text></svg>
    <svg class="wish" width="24" height="22" viewBox="0 0 24 22" fill="none" stroke="#333" stroke-width="1.8"><path d="M12 20S2 13.5 2 7a5 5 0 0 1 10-1 5 5 0 0 1 10 1c0 6.5-10 13-10 13z"/></svg>
    <div class="product-image img-roll" role="img" aria-label="Pain relief roll-on bottle"></div>
    <p class="product-desc">Lorem Ipsum is simply dummy text of the printing.</p>
    <a class="btn-cart" href="#">ADD TO CART</a>
  </article>
  <article class="product-card">
    <svg class="ribbon" width="100" height="100" viewBox="0 0 100 100"><polygon points="0,58 58,0 92,0 0,92" fill="#2f6a43"/><text x="39" y="44" transform="rotate(-45 39 39)" text-anchor="middle" font-family="Lato,sans-serif" font-weight="700" font-size="12" fill="#fff">FEATURED</text></svg>
    <svg class="wish" width="24" height="22" viewBox="0 0 24 22" fill="none" stroke="#333" stroke-width="1.8"><path d="M12 20S2 13.5 2 7a5 5 0 0 1 10-1 5 5 0 0 1 10 1c0 6.5-10 13-10 13z"/></svg>
    <div class="product-image img-pump" role="img" aria-label="CBD lotion pump bottle"></div>
    <p class="product-desc">Lorem Ipsum is simply dummy text of the printing.</p>
    <a class="btn-cart" href="#">ADD TO CART</a>
  </article>
  <article class="product-card">
    <svg class="ribbon" width="100" height="100" viewBox="0 0 100 100"><polygon points="0,58 58,0 92,0 0,92" fill="#2f6a43"/><text x="39" y="44" transform="rotate(-45 39 39)" text-anchor="middle" font-family="Lato,sans-serif" font-weight="700" font-size="12" fill="#fff">FEATURED</text></svg>
    <svg class="wish" width="24" height="22" viewBox="0 0 24 22" fill="none" stroke="#333" stroke-width="1.8"><path d="M12 20S2 13.5 2 7a5 5 0 0 1 10-1 5 5 0 0 1 10 1c0 6.5-10 13-10 13z"/></svg>
    <div class="product-image img-jar" role="img" aria-label="CBD pain relief cream jar"></div>
    <p class="product-desc">Lorem Ipsum is simply dummy text of the printing.</p>
    <a class="btn-cart" href="#">ADD TO CART</a>
  </article>
  <article class="product-card">
    <svg class="ribbon" width="100" height="100" viewBox="0 0 100 100"><polygon points="0,58 58,0 92,0 0,92" fill="#2f6a43"/><text x="39" y="45" transform="rotate(-45 39 39)" text-anchor="middle" font-family="Lato,sans-serif" font-weight="700" font-size="13" fill="#fff">NEW</text></svg>
    <svg class="wish" width="24" height="22" viewBox="0 0 24 22" fill="none" stroke="#333" stroke-width="1.8"><path d="M12 20S2 13.5 2 7a5 5 0 0 1 10-1 5 5 0 0 1 10 1c0 6.5-10 13-10 13z"/></svg>
    <div class="product-image img-bottle" role="img" aria-label="CBD capsule bottle"></div>
    <p class="product-desc">Lorem Ipsum is simply dummy text of the printing.</p>
    <a class="btn-cart" href="#">ADD TO CART</a>
  </article>
  <article class="product-card">
    <svg class="ribbon" width="100" height="100" viewBox="0 0 100 100"><polygon points="0,58 58,0 92,0 0,92" fill="#2f6a43"/><text x="39" y="45" transform="rotate(-45 39 39)" text-anchor="middle" font-family="Lato,sans-serif" font-weight="700" font-size="13" fill="#fff">NEW</text></svg>
    <svg class="wish" width="24" height="22" viewBox="0 0 24 22" fill="none" stroke="#333" stroke-width="1.8"><path d="M12 20S2 13.5 2 7a5 5 0 0 1 10-1 5 5 0 0 1 10 1c0 6.5-10 13-10 13z"/></svg>
    <div class="product-image img-roll" role="img" aria-label="Pain relief roll-on bottle"></div>
    <p class="product-desc">Lorem Ipsum is simply dummy text of the printing.</p>
    <a class="btn-cart" href="#">ADD TO CART</a>
  </article>
  <article class="product-card">
    <svg class="ribbon" width="100" height="100" viewBox="0 0 100 100"><polygon points="0,58 58,0 92,0 0,92" fill="#2f6a43"/><text x="39" y="44" transform="rotate(-45 39 39)" text-anchor="middle" font-family="Lato,sans-serif" font-weight="700" font-size="12" fill="#fff">FEATURED</text></svg>
    <svg class="wish" width="24" height="22" viewBox="0 0 24 22" fill="none" stroke="#333" stroke-width="1.8"><path d="M12 20S2 13.5 2 7a5 5 0 0 1 10-1 5 5 0 0 1 10 1c0 6.5-10 13-10 13z"/></svg>
    <div class="product-image img-pump" role="img" aria-label="CBD lotion pump bottle"></div>
    <p class="product-desc">Lorem Ipsum is simply dummy text of the printing.</p>
    <a class="btn-cart" href="#">ADD TO CART</a>
  </article>
  <article class="product-card">
    <svg class="ribbon" width="100" height="100" viewBox="0 0 100 100"><polygon points="0,58 58,0 92,0 0,92" fill="#2f6a43"/><text x="39" y="44" transform="rotate(-45 39 39)" text-anchor="middle" font-family="Lato,sans-serif" font-weight="700" font-size="12" fill="#fff">FEATURED</text></svg>
    <svg class="wish" width="24" height="22" viewBox="0 0 24 22" fill="none" stroke="#333" stroke-width="1.8"><path d="M12 20S2 13.5 2 7a5 5 0 0 1 10-1 5 5 0 0 1 10 1c0 6.5-10 13-10 13z"/></svg>
    <div class="product-image img-jar" role="img" aria-label="CBD pain relief cream jar"></div>
    <p class="product-desc">Lorem Ipsum is simply dummy text of the printing.</p>
    <a class="btn-cart" href="#">ADD TO CART</a>
  </article>
  <article class="product-card">
    <svg class="ribbon" width="100" height="100" viewBox="0 0 100 100"><polygon points="0,58 58,0 92,0 0,92" fill="#2f6a43"/><text x="39" y="45" transform="rotate(-45 39 39)" text-anchor="middle" font-family="Lato,sans-serif" font-weight="700" font-size="13" fill="#fff">NEW</text></svg>
    <svg class="wish" width="24" height="22" viewBox="0 0 24 22" fill="none" stroke="#333" stroke-width="1.8"><path d="M12 20S2 13.5 2 7a5 5 0 0 1 10-1 5 5 0 0 1 10 1c0 6.5-10 13-10 13z"/></svg>
    <div class="product-image img-bottle" role="img" aria-label="CBD capsule bottle"></div>
    <p class="product-desc">Lorem Ipsum is simply dummy text of the printing.</p>
    <a class="btn-cart" href="#">ADD TO CART</a>
  </article>
</div>

<section class="welcome">
  <h2 class="serif">WELCOME TO VERDANT LEAF</h2>
  <p class="p1">Lorem Ipsum is simply dummy text of the printing and typesetting industry. Lorem Ipsum has been the industry's standard dummy text ever since the 1500s, when an unknown printer took a galley of type and scrambled it to make a type specimen book. It has survived not only five centuries, but also the leap into electronic typesetting, remaining essentially unchanged.</p>
  <p class="p2">It was popularised in the 1960s with the release of Veltrax sheets containing Lorem Ipsum passages, and more recently with desktop publishing software like Quillset Pagecraft including versions of Lorem Ipsum.</p>
  <div class="welcome-actions"><a class="btn-light" href="#">KNOW MORE</a><a class="btn-light" href="#">SHOP NOW</a></div>
</section>

<h2 class="section-title serif" style="top:2244px">OUR PRODUCTS</h2>

<div class="product-grid" style="top:2310px">
  <article class="product-card compact">
    <svg class="wish" width="24" height="22" viewBox="0 0 24 22" fill="none" stroke="#333" stroke-width="1.8"><path d="M12 20S2 13.5 2 7a5 5 0 0 1 10-1 5 5 0 0 1 10 1c0 6.5-10 13-10 13z"/></svg>
    <div class="product-image img-roll" role="img" aria-label="Pain relief roll-on bottle"></div>
    <p class="product-desc">Lorem Ipsum is simply dummy text of the printing.</p>
    <a class="btn-cart" href="#">ADD TO CART</a>
  </article>
  <article class="product-card compact">
    <svg class="wish" width="24" height="22" viewBox="0 0 24 22" fill="none" stroke="#333" stroke-width="1.8"><path d="M12 20S2 13.5 2 7a5 5 0 0 1 10-1 5 5 0 0 1 10 1c0 6.5-10 13-10 13z"/></svg>
    <div class="product-image img-pump" role="img" aria-label="CBD lotion pump bottle"></div>
    <p class="product-desc">Lorem Ipsum is simply dummy text of the printing.</p>
    <a class="btn-cart" href="#">ADD TO CART</a>
  </article>
  <article class="product-card compact">
    <svg class="wish" width="24" height="22" viewBox="0 0 24 22" fill="none" stroke="#333" stroke-width="1.8"><path d="M12 20S2 13.5 2 7a5 5 0 0 1 10-1 5 5 0 0 1 10 1c0 6.5-10 13-10 13z"/></svg>
    <div class="product-image img-jar" role="img" aria-label="CBD pain relief cream jar"></div>
    <p class="product-desc">Lorem Ipsum is simply dummy text of the printing.</p>
    <a class="btn-cart" href="#">ADD TO CART</a>
  </article>
  <article class="product-card compact">
    <svg class="wish" width="24" height="22" viewBox="0 0 24 22" fill="none" stroke="#333" stroke-width="1.8"><path d="M12 20S2 13.5 2 7a5 5 0 0 1 10-1 5 5 0 0 1 10 1c0 6.5-10 13-10 13z"/></svg>
    <div class="product-image img-bottle" role="img" aria-label="CBD capsule bottle"></div>
    <p class="product-desc">Lorem Ipsum is simply dummy text of the printing.</p>
    <a class="btn-cart" href="#">ADD TO CART</a>
  </article>
</div>

<footer>
  <div class="footer-info">
    <div class="footer-col col-hours">
      <h3 class="serif">HOURSE OF OPERATION</h3>
      <p>MON-FRI : 7:00-22:30</p>
      <p>SAT-SUN : 7:00-22:30</p>
    </div>
    <div class="footer-col col-contact">
      <h3 class="serif">CONTACT INFO</h3>
      <p class="contact-intro">Lorem Ipsum is simply dummy text of the printing and typesetting industry.</p>
      <p>CALL US : 5550127788</p>
      <p>EMAIL US : info@verdantleaf.com</p>
    </div>
    <div class="footer-col col-social">
      <h3 class="serif">FOLLOW US ON</h3>
      <p>FRIENDWALL</p>
      <p>PHOTOGRAM</p>
      <p>CHIRPER</p>
    </div>
  </div>
  <div class="footer-bar">
    <nav class="footer-links"><a href="#">Home</a><a href="#">About us</a><a href="#">FAQ</a><a href="#">Blog</a><a href="#">Contact us</a><a href="#">Privacy policy</a><a href="#">Terms &amp; conditions</a></nav>
    <p class="copyright">©Verdant Leaf.2018 - All Rights Reserved.</p>
  </div>
</footer>

</body>
</html>
```